Health care technology software systems

We have a solid logo. We have company colors that will need to be used as well. We just need a great business card design. We sell to health plans but want to be modern
Updates

Need extra days to review

Target Market(s)

Health technology sector selling into Health Plans

Industry/Entity Type

Health Care Technology

Contact Information for Business Card

Name, title, address, phone number, email

Requirements
Must have
• Use of Kembrata corporate colors - Uploaded w/ our logos

```html
<!DOCTYPE html>
<html lang="en">
<head>
<meta charset="utf-8">
<title>Kembrata Business Card</title>
<link rel="stylesheet" href="https://fonts.googleapis.com/css2?family=Montserrat:wght@300;400;700&display=swap">
<style>
  :root {
    --backdrop: #e4e5e7;
    --card-white: #ffffff;
    --brand-blue: #1ea0de;
    --brand-blue-deep: #0f7fd0;
    --brand-aqua: #3fd0f0;
    --brand-green: #7bbf2a;
    --ink: #333333;
    --ink-soft: #4a4a4a;
  }
  * { box-sizing: border-box; margin: 0; padding: 0; }
  html, body {
    width: 1200px; height: 800px; overflow: hidden;
    background: var(--backdrop);
    font-family: "Montserrat", sans-serif;
  }
  .stage {
    width: 1200px; height: 800px;
    display: flex; align-items: center; justify-content: center; gap: 40px;
  }
  .card {
    position: relative;
    width: 540px; height: 309px;
    border-radius: 16px;
    overflow: hidden;
    box-shadow: 0 10px 24px rgba(0,0,0,0.18);
  }
  /* Front */
  .card-front { background: var(--card-white); }
  .edge-band {
    position: absolute; left: 0; right: 0; bottom: 0; height: 9px;
    background: linear-gradient(to right, var(--brand-blue) 0 60%, var(--brand-green) 60% 100%);
  }
  .wordmark {
    position: absolute; top: 70px; left: 0; right: 0;
    display: flex; align-items: center; justify-content: center; gap: 16px;
  }
  .wordmark-dot {
    width: 40px; height: 40px; border-radius: 50%;
    background: var(--brand-blue);
  }
  .wordmark-name {
    font-weight: 300; font-size: 60px; letter-spacing: 1px;
    color: var(--ink); line-height: 1;
  }
  .details {
    position: absolute; top: 168px; left: 0; right: 0;
    display: flex; justify-content: center;
  }
  .person {
    text-align: right; padding-right: 14px;
    border-right: 1px solid var(--brand-blue);
  }
  .person-name { font-weight: 700; font-size: 19px; color: var(--brand-blue); line-height: 1.1; }
  .person-title { font-weight: 400; font-size: 13px; color: var(--brand-green); margin-bottom: 6px; }
  .person-address { font-size: 11.5px; color: var(--ink-soft); line-height: 1.45; }
  .contacts { list-style: none; padding-left: 14px; }
  .contacts li {
    display: flex; align-items: center; gap: 8px;
    font-size: 11.5px; color: var(--ink-soft); line-height: 1.6;
  }
  .contacts svg { width: 11px; height: 11px; flex: none; }
  /* Back */
  .card-back { background: var(--brand-blue); }
  .back-pattern {
    position: absolute; inset: 0;
    background: linear-gradient(135deg, var(--brand-aqua) 0%, var(--brand-blue) 50%, var(--brand-blue-deep) 100%);
    opacity: 0.55;
  }
  .back-wordmark {
    position: absolute; right: 40px; bottom: 72px;
    font-weight: 300; font-size: 26px; color: var(--card-white);
  }
</style>
</head>
<body>
<main class="stage">
  <section class="card card-front" aria-label="Business card front">
    <div class="wordmark">
      <span class="wordmark-dot"></span>
      <span class="wordmark-name">kembrata</span>
    </div>
    <div class="details">
      <div class="person">
        <p class="person-name">Daniel Harper</p>
        <p class="person-title">President</p>
        <p class="person-address">4120 Juniper Court<br>Fairbanks, Alaska 34812</p>
      </div>
      <ul class="contacts">
        <li><svg viewBox="0 0 12 12"><path d="M3 1l2 2.5-1.2 1.2a7 7 0 0 0 3.5 3.5L8.5 7 11 9l-1.3 1.8C5.5 10.5 1.5 6.5 1.2 2.3z" fill="var(--brand-blue)"/></svg>555-214-7730</li>
        <li><svg viewBox="0 0 12 12"><rect x="3" y="0.8" width="6" height="10.4" rx="1" fill="none" stroke="var(--brand-blue)" stroke-width="1.4"/></svg>555-418-2093</li>
        <li><svg viewBox="0 0 12 12"><rect x="0.5" y="2" width="11" height="8" rx="1" fill="var(--brand-blue)"/><path d="M1 2.5l5 4 5-4" fill="none" stroke="#fff" stroke-width="1"/></svg>info@kembrata.com</li>
        <li><svg viewBox="0 0 12 12"><circle cx="6" cy="6" r="5.3" fill="var(--brand-blue)"/><path d="M1 6h10M6 .8c-2.5 3-2.5 7.4 0 10.4M6 .8c2.5 3 2.5 7.4 0 10.4" fill="none" stroke="#fff" stroke-width=".8"/></svg>www.kembrata.com</li>
      </ul>
    </div>
    <div class="edge-band"></div>
  </section>

  <section class="card card-back" aria-label="Business card back">
    <div class="back-pattern" role="img" aria-label="Repeating pattern of brand symbols in aqua and blue tones"></div>
    <span class="back-wordmark">kembrata</span>
  </section>
</main>
</body>
</html>
```